Card design for orthopaedic surgeons working as The Brindlewood Orthopaedic Centre

Business cards, letterhead

Colors

Designer to choose colors to be used in the design.

Requirements
Must have
• Late addition.
• Cards letterhead must have logos of
• Corvane Federated Institute of Surgeons
• Meridale Orthopaedic Society
Nice to have
• Back of card to have space for appointment time to be added by hand and some blank space for writing incidental other notes.

```html
<!DOCTYPE html>
<html lang="en">
<head>
<meta charset="utf-8">
<title>The Brindlewood Orthopaedic Centre – Business Card</title>
<link rel="stylesheet" href="https://fonts.googleapis.com/css2?family=Lato:wght@400;700&display=swap">
<style>
  :root {
    --backdrop: #ecebe8;
    --brand-blue: #54a9df;
    --accent-blue: #4a9fd8;
    --card-white: #ffffff;
    --text-grey: #5c5c5c;
    --muted-grey: #6b6b6b;
    --badge-fill: #dcebf6;
  }
  * { margin: 0; padding: 0; box-sizing: border-box; }
  html, body {
    width: 1200px; height: 900px; overflow: hidden;
    background: var(--backdrop);
    font-family: "Lato", Arial, sans-serif;
  }
  .canvas { position: relative; width: 1200px; height: 900px; }
  .card {
    position: absolute; left: 311px; width: 576px; height: 329px;
  }
  .card-front { top: 98px; background: var(--brand-blue); }
  .card-back { top: 472px; background: var(--card-white); }

  .front-wordmark {
    position: absolute; left: 0; right: 0; top: 165px;
    text-align: center; color: var(--card-white);
    font-size: 24px; font-weight: 400; letter-spacing: -0.2px;
  }
  .back-wordmark {
    position: absolute; left: 37px; top: 68px;
    color: var(--accent-blue); font-size: 18px; font-weight: 400; letter-spacing: -0.2px;
  }
  .affiliations {
    position: absolute; right: 44px; top: 48px;
    display: flex; gap: 10px;
  }
  .affiliation-badge {
    width: 40px; height: 40px; border-radius: 4px;
    background: var(--badge-fill);
  }
  .holder {
    position: absolute; right: 44px; top: 118px; text-align: right;
  }
  .holder-name { color: var(--accent-blue); font-size: 21px; font-weight: 700; line-height: 26px; }
  .holder-role { color: var(--muted-grey); font-size: 14px; line-height: 18px; }
  .divider {
    position: absolute; left: 40px; right: 44px; top: 173px;
    height: 1px; background: var(--accent-blue);
  }
  .contact-list {
    position: absolute; left: 37px; top: 196px; list-style: none;
  }
  .contact-item {
    display: flex; align-items: center; height: 23.6px;
    color: var(--text-grey); font-size: 15px;
  }
  .contact-icon { width: 17px; height: 17px; margin-right: 13px; fill: var(--accent-blue); }
  .web-name { color: var(--accent-blue); font-weight: 700; }
  .address {
    position: absolute; right: 42px; top: 245px; text-align: right;
    color: var(--accent-blue); font-size: 15px; line-height: 23px; font-style: normal;
  }
</style>
</head>
<body>
<main class="canvas">
  <section class="card card-front" aria-label="Card front">
    <p class="front-wordmark">The Brindlewood Orthopaedic Centre</p>
  </section>

  <section class="card card-back" aria-label="Card back">
    <p class="back-wordmark">The Brindlewood Orthopaedic Centre</p>

    <div class="affiliations">
      <div class="affiliation-badge" role="img" aria-label="Corvane Federated Institute of Surgeons logo"></div>
      <div class="affiliation-badge" role="img" aria-label="Meridale Orthopaedic Society logo"></div>
    </div>

    <div class="holder">
      <p class="holder-name">Dorian Vell</p>
      <p class="holder-role">Owner | Founder</p>
    </div>

    <div class="divider"></div>

    <ul class="contact-list">
      <li class="contact-item">
        <svg class="contact-icon" viewBox="0 0 24 24" aria-hidden="true"><path d="M6.6 10.8a15.5 15.5 0 0 0 6.6 6.6l2.2-2.2c.3-.3.7-.4 1-.2 1.1.4 2.3.6 3.6.6.6 0 1 .4 1 1V20c0 .6-.4 1-1 1A17 17 0 0 1 3 4c0-.6.4-1 1-1h3.5c.6 0 1 .4 1 1 0 1.2.2 2.4.6 3.6.1.3 0 .7-.2 1z"/></svg>
        +123 0071 5820
      </li>
      <li class="contact-item">
        <svg class="contact-icon" viewBox="0 0 24 24" aria-hidden="true"><path d="M5 3h9v18H5zM7 5v2h2V5zm3 0v2h2V5zM7 9v2h2V9zm3 0v2h2V9zm-3 4v2h2v-2zm3 0v2h2v-2zM15 8h4v13h-4zm1 2v2h2v-2zm0 4v2h2v-2z"/></svg>
        +123 0071 5834
      </li>
      <li class="contact-item">
        <svg class="contact-icon" viewBox="0 0 24 24" aria-hidden="true"><path d="M2 5h20v14H2zm2 2v.5l8 5 8-5V7zm0 2.8V17h16V9.8l-8 5z"/></svg>
        hello@brindlewoodortho.com
      </li>
      <li class="contact-item">
        <svg class="contact-icon" viewBox="0 0 24 24" aria-hidden="true"><path d="M12 2a10 10 0 1 0 0 20 10 10 0 0 0 0-20zm-1 17.9A8 8 0 0 1 4.1 11H7c.2 3.2 1.6 6.2 4 8.9zM7 9H4.3A8 8 0 0 1 11 4.1 13 13 0 0 0 7 9zm6 10.9c2.4-2.7 3.8-5.7 4-8.9h2.9a8 8 0 0 1-6.9 8.9zM17 9a13 13 0 0 0-4-4.9A8 8 0 0 1 19.7 9zM9 11h6c-.2 2.6-1.2 5-3 7.1-1.8-2.1-2.8-4.5-3-7.1zm0-2c.3-2 1.3-3.8 3-5.5 1.7 1.7 2.7 3.5 3 5.5z"/></svg>
        <span>www.<span class="web-name">brindlewoodortho</span>.com</span>
      </li>
    </ul>

    <address class="address">
      Harlow Lane, Eastmere<br>
      Calderby, 210
    </address>
  </section>
</main>
</body>
</html>
```